Oil and Gas Exploration and Production company needs a business card design

We need a business card design using our logo and colors in the logo. We want a mainstream design.

```html
<!DOCTYPE html>
<html lang="en">
<head>
<meta charset="utf-8">
<title>Corvan Oil &amp; Gas – Business Card</title>
<link rel="stylesheet" href="https://fonts.googleapis.com/css2?family=Arimo:ital,wght@0,400;0,700;1,700&display=swap">
<style>
  :root {
    --ink: #0b0b0b;
    --paper: #ffffff;
    --paper-shade: #ececec;
    --gold: #c9a227;
    --gold-deep: #a98514;
    --gold-light: #e3c455;
    --stage: #e6e3dd;
  }
  * { box-sizing: border-box; margin: 0; padding: 0; }
  html, body {
    width: 1200px; height: 780px; overflow: hidden;
    background: var(--stage);
    font-family: "Arimo", Arial, sans-serif;
  }
  .sheet {
    position: relative; width: 1200px; height: 780px;
    display: flex; justify-content: center; align-items: center; gap: 110px;
  }
  .card {
    position: relative; width: 343px; height: 600px;
    border-radius: 18px; overflow: hidden;
    background: linear-gradient(180deg, var(--paper) 0%, var(--paper-shade) 100%);
    box-shadow: 0 10px 28px rgba(0,0,0,.22);
  }
  /* brand lockup */
  .brand {
    position: absolute; left: 0; right: 0;
    display: flex; align-items: center; justify-content: center; gap: 12px;
    color: var(--ink); font-weight: 700;
  }
  .brand-dot { border-radius: 50%; background: var(--gold); flex: none; }
  .brand-name { line-height: 1.05; text-align: left; }

  .card-front .brand { top: 84px; }
  .card-front .brand-dot { width: 34px; height: 34px; }
  .card-front .brand-name { font-size: 30px; }

  .card-back .brand { top: 268px; }
  .card-back .brand-dot { width: 44px; height: 44px; }
  .card-back .brand-name { font-size: 36px; }

  .front-art { position: absolute; left: 0; top: 0; width: 343px; height: 600px; }

  .contact {
    position: absolute; right: 30px; left: 30px; top: 306px;
    text-align: right; color: var(--paper);
  }
  .person-name { font-size: 22px; font-weight: 700; letter-spacing: .3px; line-height: 1.15; }
  .person-role { font-size: 17px; color: var(--gold); margin-top: 2px; line-height: 1.15; }
  .rule {
    height: 1px; margin: 10px 0 7px auto; width: 88%;
    background: linear-gradient(90deg, transparent, var(--gold) 40%, var(--gold));
  }
  .label { font-size: 13px; font-weight: 700; font-style: italic; color: var(--gold); line-height: 1.15; }
  .value { font-size: 15.5px; margin-top: 2px; line-height: 1.15; }
  .address { font-size: 15.5px; line-height: 1.35; margin-top: 4px; }

  .web-band {
    position: absolute; left: 0; right: 0; bottom: 0; height: 60px;
    display: flex; align-items: center; justify-content: center;
    color: var(--ink); font-size: 17px;
    background: linear-gradient(180deg, var(--gold-light), var(--gold) 55%, var(--gold-deep));
    border-top: 5px solid var(--paper);
  }
</style>
</head>
<body>
<main class="sheet">

  <section class="card card-front" aria-label="Business card front">
    <svg class="front-art" viewBox="0 0 343 600" aria-hidden="true">
      <path d="M0 206 C 110 214, 260 232, 343 284 L 343 600 L 0 600 Z" fill="#c9a227"/>
      <path d="M0 216 C 110 224, 255 242, 343 294 L 343 600 L 0 600 Z" fill="#0b0b0b"/>
      <path d="M150 240 C 225 246, 300 262, 343 288 C 295 268, 230 254, 150 240 Z" fill="#ffffff"/>
    </svg>

    <div class="brand">
      <span class="brand-dot"></span>
      <span class="brand-name">Corvan<br>Oil &amp; Gas</span>
    </div>

    <div class="contact">
      <p class="person-name">Marcus Hale</p>
      <p class="person-role">Marketing Officer</p>
      <div class="rule"></div>
      <p class="label">Cell:</p>
      <p class="value">(123) 555 0142</p>
      <div class="rule"></div>
      <p class="label">Email:</p>
      <p class="value">info@corvanenergy.com</p>
      <div class="rule"></div>
      <p class="address">PO Box 48, Harbour Road<br>4th Lane, Leeds</p>
    </div>

    <div class="web-band">www.corvanenergy.com</div>
  </section>

  <section class="card card-back" aria-label="Business card back">
    <div class="brand">
      <span class="brand-dot"></span>
      <span class="brand-name">Corvan<br>Oil &amp; Gas</span>
    </div>
  </section>

</main>
</body>
</html>
```